Real Estate Entrepreneur needs a business card

I am a real estate entrepreneur, I buy houses for investment purposes, I act as a real estate agent representing buyers and sellers in residential home transactions, I am a contractor that does a wide range of home repairs and construction. I'd like a design that can stick with me through the years as my business grows and morphs to fit any niche I decide to pursue as markets change.

Target Market(s)

Anyone with interest that may be related to real estate.

Industry/Entity Type

Real Estate

Contact Information for Business Card

A card that stands out and doesn't put me in any one box. My business will evolve over time and I need a card that can stay relevant.

Colors

Designer to choose colors to be used in the design.

Requirements
Must have
• Character
Nice to have
• I'm open
Should not have
• Cliche houses and hammers

```html
<!DOCTYPE html>
<html lang="en">
<head>
<meta charset="utf-8">
<title>Reed Holloway – Business Card</title>
<link href="https://fonts.googleapis.com/css2?family=Raleway:wght@400;500;600&display=swap" rel="stylesheet">
<style>
  :root {
    --stage: #1f1f21;
    --ink: #0c0c0d;
    --paper: #e3e5eb;
    --line: #e8e8ec;
    --art-dark: #1a1a1c;
    --art-light: #d9dbe2;
  }
  * { box-sizing: border-box; margin: 0; padding: 0; }
  html, body {
    width: 1200px; height: 797px; overflow: hidden;
    background: var(--stage);
    font-family: "Raleway", sans-serif;
  }
  .stage {
    position: relative; width: 1200px; height: 797px;
    display: flex; align-items: center; justify-content: center; gap: 50px;
  }
  .card {
    position: relative; width: 520px; height: 300px; overflow: hidden;
    box-shadow: 0 12px 30px rgba(0,0,0,.45);
  }

  /* Front */
  .card--front { background: var(--ink); color: var(--line); }
  .rule {
    position: absolute; left: 0; right: 0; height: 2px; background: var(--line);
  }
  .rule--top { top: 14px; }
  .rule--bottom { bottom: 14px; }
  .name-box {
    position: absolute; left: 34px; top: 52px;
    border: 1.5px solid var(--line); padding: 8px 14px 8px 12px;
  }
  .name-box__rule {
    position: absolute; left: 40px; right: -4px; top: -7px; height: 1.5px; background: var(--line);
  }
  .name {
    font-weight: 400; font-size: 27px; letter-spacing: .5px; line-height: 1.1;
  }
  .role { font-weight: 500; font-size: 16px; line-height: 1.3; }
  .contacts {
    position: absolute; left: 40px; top: 172px; list-style: none;
    font-weight: 600; font-size: 17px;
  }
  .contacts li { display: flex; align-items: center; gap: 12px; height: 32px; }
  .contacts svg { width: 20px; height: 20px; flex: none; }
  .phone { font-size: 19px; letter-spacing: 1px; }
  .key-art {
    position: absolute; right: 30px; top: 38px; width: 150px; height: 210px;
    background: linear-gradient(160deg, var(--art-light), #b9bcc5);
    opacity: .9;
  }

  /* Back */
  .card--back { background: var(--paper); }
  .band { position: absolute; left: 0; right: 0; background: var(--ink); }
  .band--top { top: 0; height: 12px; }
  .band--bottom { bottom: 0; height: 16px; }
  .sign-art {
    position: absolute; left: 175px; top: 78px; width: 180px; height: 160px;
    background: linear-gradient(160deg, var(--art-dark), #3a3a3e);
  }
</style>
</head>
<body>
<main class="stage">
  <section class="card card--front">
    <div class="rule rule--top"></div>
    <div class="name-box">
      <div class="name-box__rule"></div>
      <h1 class="name">REED HOLLOWAY</h1>
      <p class="role">Real estate entrepreneur</p>
    </div>
    <ul class="contacts">
      <li>
        <svg viewBox="0 0 20 20" fill="none" stroke="currentColor" stroke-width="1.5"><rect x="6" y="2" width="8" height="16" rx="1.5"/><line x1="9" y1="15.5" x2="11" y2="15.5"/></svg>
        <span class="phone">00 000 000</span>
      </li>
      <li>
        <svg viewBox="0 0 20 20" fill="none" stroke="currentColor" stroke-width="1.3"><rect x="1.5" y="4.5" width="17" height="11"/><polyline points="1.5,4.5 10,11 18.5,4.5"/></svg>
        <span>hello@reedholloway.com</span>
      </li>
      <li>
        <svg viewBox="0 0 20 20" fill="currentColor"><path d="M10 1.5a5.5 5.5 0 0 0-5.5 5.5c0 4.2 5.5 11.5 5.5 11.5s5.5-7.3 5.5-11.5A5.5 5.5 0 0 0 10 1.5zm0 7.7a2.2 2.2 0 1 1 0-4.4 2.2 2.2 0 0 1 0 4.4z"/></svg>
        <span>address</span>
      </li>
    </ul>
    <div class="key-art" role="img" aria-label="Illustration of a house key on a ring with a blank key tag"></div>
    <div class="rule rule--bottom"></div>
  </section>

  <section class="card card--back">
    <div class="band band--top"></div>
    <div class="sign-art" role="img" aria-label="Illustration of a hanging real estate sign post holding the logo panel"></div>
    <div class="band band--bottom"></div>
  </section>
</main>
</body>
</html>
```